Chicken Wing A0 and A4 Poster

Our restaurant name is Tovvra Grill

We have introduced chicken wings to our menu. They are deep fried and mixed with different sauce selections.

The sauce options are: Tovvra BBQ, Regular BBQ, Sweet Chili and Garlic, Hot Chili, Garlic

Available in a 6, 10 or 20 Pack.
Larger Catering Packs Available

We have uploaded some pictures from the internet with chicken wings.

We also have 4 other poster designs coming in the next 3 weeks.

Industry/Entity Type

Restaurant

```html
<!DOCTYPE html>
<html lang="en">
<head>
<meta charset="utf-8">
<title>Tovvra Grill – Chicken Wings Poster</title>
<link href="https://fonts.googleapis.com/css2?family=Poppins:wght@600;700;800&display=swap" rel="stylesheet">
<style>
  :root {
    --canvas-grey: #d6d6d6;
    --paper: #ffffff;
    --crimson: #a8062f;
    --crimson-deep: #7d0022;
    --wing-orange: #d9601e;
    --wing-amber: #f08a3a;
    --wing-brown: #8c2e10;
    --ink-light: #ffffff;
  }
  * { margin: 0; padding: 0; box-sizing: border-box; }
  html, body {
    width: 1200px; height: 1000px; overflow: hidden;
    background: var(--canvas-grey);
    font-family: "Poppins", "Helvetica Neue", Arial, sans-serif;
  }
  .poster {
    position: absolute; left: 332px; top: 122px;
    width: 534px; height: 756px;
    background: var(--paper);
    overflow: hidden;
  }
  .poster-shapes { position: absolute; inset: 0; }
  .brand {
    position: absolute; left: 0; right: 0; top: 56px;
    display: flex; flex-direction: column; align-items: center;
    color: var(--crimson);
  }
  .brand-name {
    font-size: 48px; font-weight: 800; letter-spacing: -1px; line-height: 1;
  }
  .brand-tagline {
    margin-top: 4px;
    font-size: 12px; font-weight: 800; letter-spacing: 2.5px; line-height: 1;
    text-transform: uppercase;
  }
  .menu-info {
    position: absolute; left: 33px; top: 520px; right: 20px;
    color: var(--ink-light);
  }
  .menu-heading { font-size: 26px; font-weight: 700; line-height: 30px; }
  .sauce-list {
    margin-top: 6.5px; font-size: 16px; font-weight: 600; line-height: 19px;
  }
  .pack-sizes {
    margin-top: 34.5px; font-size: 28px; font-weight: 700; line-height: 32px;
  }
  .catering-note { margin-top: 4px; font-size: 16px; font-weight: 600; line-height: 20px; }
</style>
</head>
<body>
  <main class="poster">
    <svg class="poster-shapes" width="534" height="756" viewBox="0 0 534 756" xmlns="http://www.w3.org/2000/svg">
      <defs>
        <linearGradient id="wingTones" x1="0" y1="0" x2="1" y2="1">
          <stop offset="0" stop-color="var(--wing-brown)"/>
          <stop offset="0.35" stop-color="var(--wing-orange)"/>
          <stop offset="0.6" stop-color="var(--wing-amber)"/>
          <stop offset="1" stop-color="var(--wing-brown)"/>
        </linearGradient>
        <linearGradient id="panelShade" x1="0" y1="0" x2="0" y2="1">
          <stop offset="0" stop-color="var(--crimson-deep)"/>
          <stop offset="0.22" stop-color="var(--crimson)"/>
          <stop offset="1" stop-color="var(--crimson)"/>
        </linearGradient>
      </defs>
      <g class="hero-photo" role="img" aria-label="Photo of glazed barbecue chicken wings piled on a plate">
        <polygon points="0,186 534,126 534,420 0,480" fill="url(#wingTones)"/>
      </g>
      <polygon class="divider-top" points="0,178 534,117 534,128 0,189" fill="var(--crimson)"/>
      <polygon class="info-panel" points="0,486 534,424 534,756 0,756" fill="url(#panelShade)"/>
      <polygon class="divider-bottom" points="0,477 534,415 534,425 0,487" fill="var(--crimson)"/>
    </svg>

    <header class="brand">
      <span class="brand-name">Tovvra Grill</span>
      <p class="brand-tagline">Authentic Lebanese Food</p>
    </header>

    <section class="menu-info">
      <h2 class="menu-heading">SAUCE OPTIONS:</h2>
      <p class="sauce-list">Tovvra BBQ, Regular BBQ, Sweet Chili and Garlic,<br>Hot Chili, Garlic.</p>
      <p class="pack-sizes">Available in a 6, 10 or 20 Pack.</p>
      <p class="catering-note">Larger Catering Packs Available</p>
    </section>
  </main>
</body>
</html>
```